Header for Academic Handouts (How-to-Guides)

We are looking for a design element, which can be used as a visual header on A4-word-documents (Portrait-Set-Up). It shall be a graphic, visual language which is clearly understandable. The header height shall be between 0.75 - 1.5 inch – so it should not have too many small details. Attached below ideas/directions how the final document could look like.

The visual element shall symbolize by simple means the topic of “flipped classroom” or “active learning”. The documents with these new graphic elements will be used on handouts which are distributed in this training course:
https://www.korvanel.ch/en/the-korvanel-academy/education/educational-development/didaktische-weiterbildung/flipped-classroom.html

```html
<!DOCTYPE html>
<html lang="en">
<head>
<meta charset="utf-8">
<title>Flipped Classroom – Handout Header</title>
<link rel="stylesheet" href="https://fonts.googleapis.com/css2?family=Roboto+Condensed:wght@700&display=swap">
<style>
  :root {
    --brand-blue: #1e58a8;
    --band-grey: #cbc8c8;
    --accent-blue: #6f8fe0;
    --paper: #ffffff;
    --title-white: #ffffff;
  }
  html, body {
    margin: 0;
    padding: 0;
    overflow: hidden;
    background: var(--paper);
  }
  .page {
    position: relative;
    width: 927px;
    height: 1200px;
    overflow: hidden;
    background: var(--paper);
  }
  .header-band {
    position: absolute;
    left: 0;
    top: 0;
    width: 927px;
    height: 130px;
  }
  .header-title {
    position: absolute;
    left: 462px;
    top: 52px;
    margin: 0;
    font-family: "Roboto Condensed", "Arial Narrow", sans-serif;
    font-weight: 700;
    font-size: 45px;
    line-height: 1;
    letter-spacing: -0.5px;
    color: var(--title-white);
    white-space: nowrap;
  }
  .footer-rule {
    position: absolute;
    left: 0;
    top: 1182px;
    width: 927px;
    height: 9px;
    background: var(--brand-blue);
  }
</style>
</head>
<body>
<div class="page">
  <svg class="header-band" viewBox="0 0 927 130" aria-hidden="true">
    <defs>
      <filter id="panel-shadow" x="-5%" y="-10%" width="110%" height="130%">
        <feDropShadow dx="1" dy="2" stdDeviation="1.5" flood-color="#000" flood-opacity="0.35"/>
      </filter>
    </defs>
    <rect class="grey-strip" x="0" y="11" width="927" height="115" fill="var(--band-grey)"/>
    <polygon class="blue-panel" points="399,7 924,7 924,121 446,121" fill="var(--brand-blue)" filter="url(#panel-shadow)"/>
    <rect class="title-marker" x="330" y="50" width="44" height="44" fill="var(--accent-blue)"/>
  </svg>
  <h1 class="header-title">FLIPPED CLASSROOM</h1>
  <div class="footer-rule"></div>
</div>
</body>
</html>
```